Business Card Design

Melodex Podcast

Industry/Entity Type

Business

Contact Information for Business Card

YOU ARE INVITED TO LISTEN
Stretch Every Idea
Award Winning Melodex Podcast
with Dr. Marla Quenby
www.drmarlaquenby-example.com

555-018-7364

```html
<!DOCTYPE html>
<html lang="en">
<head>
<meta charset="utf-8">
<title>Melodex Podcast – Business Card</title>
<link rel="stylesheet" href="https://fonts.googleapis.com/css2?family=Righteous&family=Questrial&display=swap">
<style>
  :root {
    --page-bg: #e6e6e6;
    --card-light: #c6e07a;
    --card-mid: #acd152;
    --card-dark: #94c23a;
    --ink: #111111;
    --mic-light: #f2f2f2;
    --mic-mid: #a9a9a9;
    --mic-dark: #4a4a4a;
  }
  * { margin: 0; padding: 0; box-sizing: border-box; }
  html, body {
    width: 1200px;
    height: 898px;
    overflow: hidden;
    background: var(--page-bg);
  }
  .stage {
    width: 1200px;
    height: 898px;
    display: flex;
    align-items: center;
    justify-content: center;
  }
  .business-card {
    position: relative;
    width: 1000px;
    height: 572px;
    background: linear-gradient(160deg, var(--card-light) 0%, var(--card-mid) 55%, var(--card-dark) 100%);
    overflow: hidden;
    box-shadow: 0 6px 18px rgba(0,0,0,0.18);
  }
  .headline {
    position: absolute;
    left: 60px;
    top: 78px;
    width: 560px;
    font-family: "Righteous", "Arial Black", sans-serif;
    font-size: 48px;
    line-height: 60px;
    font-weight: 400;
    color: var(--ink);
    letter-spacing: 1px;
  }
  .headline span { display: block; white-space: nowrap; }
  .headline .line-1 { padding-left: 36px; }
  .host-line {
    position: absolute;
    left: 96px;
    top: 352px;
    font-family: "Righteous", "Arial Black", sans-serif;
    font-size: 28px;
    color: var(--ink);
    letter-spacing: 0.5px;
    white-space: nowrap;
  }
  .contact {
    position: absolute;
    left: 96px;
    top: 420px;
    font-family: "Questrial", "Century Gothic", sans-serif;
    font-size: 28px;
    color: var(--ink);
    list-style: none;
  }
  .contact li {
    display: flex;
    align-items: center;
    gap: 12px;
    height: 48px;
    white-space: nowrap;
  }
  .contact svg { width: 30px; height: 30px; flex: none; }
  .microphone-photo {
    position: absolute;
    left: 670px;
    top: 30px;
    width: 300px;
    height: 560px;
    border-radius: 150px 150px 50px 50px;
    background: radial-gradient(ellipse at 40% 30%, var(--mic-light) 0%, var(--mic-mid) 50%, var(--mic-dark) 100%);
  }
</style>
</head>
<body>
  <main class="stage">
    <section class="business-card">
      <div class="microphone-photo" role="img" aria-label="Photograph of a chrome vintage studio microphone"></div>

      <h1 class="headline">
        <span class="line-1">YOU ARE INVITED</span>
        <span class="line-2">TO LISTEN Stretch</span>
        <span class="line-3">Every Idea Award</span>
        <span class="line-4">Winning Melodex</span>
      </h1>

      <p class="host-line">Podcast with Dr. Marla Quenby</p>

      <ul class="contact">
        <li class="contact-phone">
          <svg viewBox="0 0 32 32" aria-hidden="true">
            <path d="M9 4 L13 10 L10.5 13 C12 17 15 20 19 21.5 L22 19 L28 23 L25.5 28 C15 28 4 17 4 6.5 Z" fill="none" stroke="var(--ink)" stroke-width="2.6" stroke-linejoin="round"/>
            <path d="M19 7 A6 6 0 0 1 25 13 M19 2.5 A10.5 10.5 0 0 1 29.5 13" fill="none" stroke="var(--ink)" stroke-width="2.2"/>
          </svg>
          <span>555-018-7364</span>
        </li>
        <li class="contact-web">
          <svg viewBox="0 0 32 32" aria-hidden="true">
            <rect x="3" y="4" width="26" height="24" rx="2" fill="none" stroke="var(--ink)" stroke-width="2.6"/>
            <line x1="3" y1="10" x2="29" y2="10" stroke="var(--ink)" stroke-width="2.6"/>
            <rect x="7" y="14" width="8" height="10" fill="var(--ink)"/>
            <line x1="18" y1="15" x2="26" y2="15" stroke="var(--ink)" stroke-width="2"/>
            <line x1="18" y1="19" x2="26" y2="19" stroke="var(--ink)" stroke-width="2"/>
            <line x1="18" y1="23" x2="26" y2="23" stroke="var(--ink)" stroke-width="2"/>
          </svg>
          <span>www.drmarlaquenby-example.com</span>
        </li>
      </ul>
    </section>
  </main>
</body>
</html>
```